Asia Hotel need a card and logo

The new hotel in East Asia, Taiwan need a business card and logo design.The hotel's Chinese name is 岚柏文旅,English name is "Velmira Hotel".The core concept of this hotel is "Eco green", going to use many plant etc.,The building's first outlook draft is attached in the file for your reference.The style be modern and fashion will be good. Thank you.
Target Market(s)
East Asia
Industry/Entity Type
Hotel
Contact Information for Business Card
The hotel's name both in Chinese and English :岚柏商旅 Velmira Hotel
The logo, address, E-mail and tel number place.
Stuff's name and title.
Font styles to use
Colors
Designer to choose colors to be used in the design.
Look and feel
Each slider illustrates characteristics of the customer's brand and the style your logo design should communicate.

```html
<!DOCTYPE html>
<html lang="en">
<head>
<meta charset="utf-8">
<title>Velmira Hotel — Business Card</title>
<link rel="stylesheet" href="https://fonts.googleapis.com/css2?family=Poppins:wght@600&family=Noto+Serif:wght@700&family=Noto+Sans+TC:wght@300&display=swap">
<style>
  :root {
    --bg: #e4e4e4;
    --paper: #f4f4f4;
    --charcoal: #1e2224;
    --ink: #111314;
    --green: #118a2c;
    --green-deep: #04570f;
    --white: #ffffff;
  }
  html, body { margin: 0; padding: 0; overflow: hidden; }
  body {
    width: 1200px; height: 1000px;
    background: var(--bg);
    position: relative;
  }
  .card {
    position: absolute;
    left: 240px;
    width: 720px; height: 400px;
    overflow: hidden;
    box-shadow: 0 10px 30px rgba(0,0,0,.18);
  }
  .card--back { top: 70px; background: var(--paper); }
  .card--front { top: 530px; background: var(--charcoal); }
  .card__art { position: absolute; inset: 0; }

  .card__pattern-area {
    position: absolute; inset: 0;
    background: linear-gradient(90deg, var(--green-deep) 0%, var(--green) 45%, #0d3a17 100%);
    clip-path: polygon(0 0, 480px 0, 300px 400px, 0 400px);
  }

  .contact-list {
    position: absolute; left: 48px; top: 56px;
    margin: 0; padding: 0; list-style: none;
  }
  .contact-list__item {
    display: flex; align-items: center; gap: 22px;
    height: 34px; margin-bottom: 52px;
    font-family: "Poppins", sans-serif; font-weight: 600;
    font-size: 16px; letter-spacing: 1.5px; color: var(--ink);
  }
  .contact-list__icon { width: 30px; height: 30px; fill: var(--ink); flex: none; }

  .brand {
    position: absolute; text-align: center; color: var(--white);
  }
  .card--back .brand { right: 22px; top: 46px; width: 250px; }
  .card--front .brand { right: 30px; top: 92px; width: 320px; }
  .brand__mark {
    display: block; margin: 0 auto 22px;
    width: 110px; height: 110px; border-radius: 50%;
    border: 5px solid var(--white); box-sizing: border-box;
  }
  .card--back .brand__mark { width: 100px; height: 100px; margin-bottom: 18px; }
  .brand__name-en {
    font-family: "Noto Serif", serif; font-weight: 700;
    font-size: 34px; line-height: 1.1; margin: 0; letter-spacing: .5px;
    white-space: nowrap;
  }
  .card--back .brand__name-en { font-size: 29px; }
  .brand__name-zh {
    font-family: "Noto Sans TC", sans-serif; font-weight: 300;
    font-size: 30px; line-height: 1.3; margin: 0; letter-spacing: 2px;
  }
  .card--back .brand__name-zh { font-size: 26px; }
</style>
</head>
<body>

<section class="card card--back" aria-label="Business card, contact side">
  <svg class="card__art" viewBox="0 0 720 400" aria-hidden="true">
    <path d="M470 0 C 370 60, 360 330, 460 400 L720 400 L720 0 Z" fill="var(--green)"/>
    <path d="M500 0 C 395 70, 390 330, 490 400 L720 400 L720 0 Z" fill="var(--charcoal)"/>
  </svg>

  <ul class="contact-list">
    <li class="contact-list__item">
      <svg class="contact-list__icon" viewBox="0 0 24 24"><path d="M12 2a7 7 0 0 0-7 7c0 5 7 13 7 13s7-8 7-13a7 7 0 0 0-7-7zm0 9.5A2.5 2.5 0 1 1 12 6.5a2.5 2.5 0 0 1 0 5z"/></svg>
      TAIWAIN, CHINESE
    </li>
    <li class="contact-list__item">
      <svg class="contact-list__icon" viewBox="0 0 24 24"><path d="M6.6 10.8a15 15 0 0 0 6.6 6.6l2.2-2.2a1 1 0 0 1 1-.25 11.4 11.4 0 0 0 3.6.57 1 1 0 0 1 1 1V20a1 1 0 0 1-1 1A17 17 0 0 1 3 4a1 1 0 0 1 1-1h3.5a1 1 0 0 1 1 1c0 1.250.2 2.45.57 3.57a1 1 0 0 1-.25 1z"/></svg>
      01750 318 462
    </li>
    <li class="contact-list__item">
      <svg class="contact-list__icon" viewBox="0 0 24 24"><path d="M2 5h20v14H2z M3.5 6.5 12 13l8.5-6.5" fill="none" stroke="var(--ink)" stroke-width="1.6"/><path d="M2 5h20L12 13z"/></svg>
      VELMIRAHOTEL@MAIL.COM
    </li>
  </ul>

  <div class="brand">
    <span class="brand__mark" aria-hidden="true"></span>
    <p class="brand__name-en">Velmira Hotel</p>
    <p class="brand__name-zh">岚柏商旅</p>
  </div>
</section>

<section class="card card--front" aria-label="Business card, brand side">
  <div class="card__pattern-area" role="img" aria-label="Decorative pattern of green and black flowing bands"></div>

  <div class="brand">
    <span class="brand__mark" aria-hidden="true"></span>
    <p class="brand__name-en">Velmira Hotel</p>
    <p class="brand__name-zh">岚柏商旅</p>
  </div>
</section>

</body>
</html>
```